Progressive European Honey Business needs minimalistic packaging design

Hello - thank you for your interest in our brief. We are Velvet Jinx, a London based Honey business, importing only the best honey Europe has to offer. Our values are deeply rooted with in progressive liberal values and we are looking for minimalist packaging, which reflects that.

We are looking for a design, which dimensions fit with our packaging option (Kelmor Glass Jar | HEIGHT 90mm | DIAMETER 63mm). We will require a various output files (High Resolution JPEG (CMYK Colors 300 dpi) Source File Ai, PSD, PDF, Printing files (die cut, die folding) and a 3D Mockup of the packaging for use within digital commerce platforms.

We must be able to adjust the free text on the label front and it should include the following:
Brand Name
Honey type
Limited edition No. X / 100 ( X being the number of purchase i.e. 25 / 100)
EU Honey, Single Orgin (Germany)
(c) The net weight (250g)

The back must include room for additional information (again adjustable by us) and the following:
“Unsuitable for children under 12 months”
(b) The appropriate durability declaration

In total, we are looking for
a) A front label
b) A back label
c) A seal (round) including the attached bee and logo included in the Zip file.
Do note that a) & b) can also be combined into one design as long as the symmetry on the jar stays intact.

The final design should communicate modern aesthetics, high quality, that are slightly provocative and pop off the shelves.
Updates

Hi folks, sorry for the delay in completing this project, but my business partner had a leak in his house. We planned to finalise our review today, but this will have to wait until it's no longer raining in his livingroom. Our sincere apologies!

Other font styles liked:
• See branding guidelines

Requirements
Must have
• Must follow the branding guideline and fonts provided as attachment

```html
<!DOCTYPE html>
<html lang="en">
<head>
<meta charset="utf-8">
<title>Velvet Jinx – Front Label</title>
<link rel="stylesheet" href="https://fonts.googleapis.com/css2?family=Roboto+Condensed:wght@400;700&family=Roboto+Mono:wght@500;700&display=swap">
<style>
  :root {
    --page: #ececec;
    --label: #ffffff;
    --orange: #e8733a;
    --orange-soft: #f3b08a;
    --purple: #8a3a96;
    --ink: #1c1c1c;
    --wash-grey: #d6dfe0;
    --wash-pink: #efd4dc;
  }
  html, body {
    margin: 0;
    padding: 0;
    width: 1061px;
    height: 1200px;
    overflow: hidden;
    background: var(--page);
  }
  .canvas {
    position: relative;
    width: 1061px;
    height: 1200px;
  }
  .front-label {
    position: absolute;
    left: 115px;
    top: 100px;
    width: 830px;
    height: 1000px;
    box-shadow: 0 6px 24px rgba(0,0,0,0.12);
  }
  .front-label svg { display: block; }
  .brand-name {
    font-family: "Roboto Condensed", sans-serif;
    font-weight: 700;
    font-size: 66px;
    fill: var(--purple);
  }
  .type-label {
    font-family: "Roboto Condensed", sans-serif;
    font-weight: 700;
    font-size: 30px;
    letter-spacing: 1px;
    fill: var(--label);
  }
  .type-value {
    font-family: "Roboto Condensed", sans-serif;
    font-weight: 700;
    font-size: 34px;
    letter-spacing: 2px;
    fill: var(--purple);
  }
  .est-text {
    font-family: "Roboto Condensed", sans-serif;
    font-weight: 700;
    fill: var(--label);
  }
  .edition-text {
    font-family: "Roboto Condensed", sans-serif;
    font-weight: 700;
    font-size: 20px;
    letter-spacing: 1px;
    fill: var(--label);
  }
  .origin-text {
    font-family: "Roboto Mono", monospace;
    font-weight: 700;
    font-size: 17px;
    fill: var(--ink);
  }
  .weight-text {
    font-family: "Roboto Mono", monospace;
    font-weight: 500;
    font-size: 13px;
    fill: var(--label);
  }
</style>
</head>
<body>
<div class="canvas">
  <div class="front-label">
    <svg width="830" height="1000" viewBox="0 0 830 1000" xmlns="http://www.w3.org/2000/svg">
      <defs>
        <linearGradient id="washGradient" x1="0" y1="0" x2="0" y2="1">
          <stop offset="0" stop-color="#ffffff"/>
          <stop offset="0.15" stop-color="#d6dfe0"/>
          <stop offset="0.7" stop-color="#d6dfe0"/>
          <stop offset="0.82" stop-color="#efd4dc"/>
          <stop offset="1" stop-color="#ffffff"/>
        </linearGradient>
        <linearGradient id="ornamentGradient" x1="0" y1="0" x2="1" y2="1">
          <stop offset="0" stop-color="#f3b08a"/>
          <stop offset="1" stop-color="#ec8a55"/>
        </linearGradient>
      </defs>

      <!-- label sheet -->
      <rect class="label-sheet" x="0" y="0" width="830" height="1000" fill="var(--label)"/>

      <!-- landscape wash -->
      <rect class="landscape-wash" x="0" y="40" width="830" height="920" fill="url(#washGradient)"
            role="img" aria-label="Soft watercolour landscape with trees and white flowers"/>

      <!-- corner flourishes, kept outside the oval -->
      <rect class="flourish" x="34" y="26" width="150" height="160" rx="40" fill="url(#ornamentGradient)"
            role="img" aria-label="Orange and black scroll flourish, top left"/>
      <rect class="flourish" x="646" y="26" width="150" height="160" rx="40" fill="url(#ornamentGradient)"
            role="img" aria-label="Orange and black scroll flourish, top right"/>
      <rect class="flourish" x="34" y="820" width="130" height="152" rx="40" fill="url(#ornamentGradient)"
            role="img" aria-label="Orange and black scroll flourish, bottom left"/>
      <rect class="flourish" x="666" y="820" width="130" height="152" rx="40" fill="url(#ornamentGradient)"
            role="img" aria-label="Orange and black scroll flourish, bottom right"/>

      <!-- top and bottom edge lines -->
      <rect class="edge-line" x="0" y="10" width="830" height="4" fill="var(--orange)"/>
      <rect class="edge-line" x="0" y="986" width="830" height="4" fill="var(--orange)"/>

      <!-- oval frame -->
      <ellipse class="oval-frame" cx="416" cy="525" rx="322" ry="455" fill="none" stroke="var(--ink)" stroke-width="3"/>

      <!-- title panel -->
      <g class="title-panel">
        <rect x="126" y="270" width="570" height="440" fill="var(--label)" stroke="var(--ink)" stroke-width="6"/>
        <rect x="140" y="284" width="542" height="412" fill="none" stroke="var(--orange)" stroke-width="6"/>
        <rect x="152" y="296" width="518" height="388" fill="none" stroke="var(--ink)" stroke-width="2"/>
      </g>

      <!-- brand mark: plain circle -->
      <circle class="brand-circle" cx="416" cy="262" r="88" fill="var(--ink)" stroke="var(--orange)" stroke-width="8"/>

      <!-- brand name -->
      <text class="brand-name" x="416" y="480" text-anchor="middle">Velvet Jinx</text>

      <!-- divider with drop -->
      <g class="divider">
        <rect x="200" y="530" width="180" height="3" fill="var(--orange)"/>
        <rect x="452" y="530" width="180" height="3" fill="var(--orange)"/>
        <path d="M416 516 C410 528 406 534 406 540 A10 10 0 0 0 426 540 C426 534 422 528 416 516 Z" fill="var(--purple)"/>
      </g>

      <!-- honey type -->
      <rect class="type-band" x="162" y="570" width="498" height="46" fill="var(--purple)"/>
      <text class="type-label" x="411" y="604" text-anchor="middle">HONEY TYPE</text>
      <text class="type-value" x="411" y="664" text-anchor="middle">XXXXX</text>

      <!-- established badge -->
      <g class="est-badge">
        <path d="M150 704 L676 704 L620 760 L416 840 L212 760 Z" fill="var(--ink)"/>
        <path d="M190 716 L330 716 L330 730 L208 730 Z" fill="var(--orange)"/>
        <path d="M502 716 L642 716 L624 730 L502 730 Z" fill="var(--orange)"/>
        <path d="M340 790 L492 790 L416 822 Z" fill="var(--orange)"/>
        <rect x="372" y="712" width="88" height="74" fill="none" stroke="var(--label)" stroke-width="2"/>
        <text class="est-text" x="416" y="742" text-anchor="middle" font-size="22" letter-spacing="6">EST</text>
        <rect x="380" y="750" width="72" height="2" fill="var(--label)"/>
        <text class="est-text" x="416" y="778" text-anchor="middle" font-size="24" letter-spacing="2">1957</text>
      </g>

      <!-- edition and origin -->
      <rect class="edition-band" x="200" y="848" width="432" height="28" fill="var(--orange)"/>
      <text class="edition-text" x="416" y="869" text-anchor="middle">LIMITED EDITION NO.X</text>
      <text class="origin-text" x="416" y="902" text-anchor="middle">EU HONEY</text>
      <text class="origin-text" x="416" y="926" text-anchor="middle">SINGLE ORGIN (GERMANY)</text>
      <rect class="weight-band" x="276" y="938" width="280" height="22" fill="var(--orange)"/>
      <text class="weight-text" x="416" y="954" text-anchor="middle">NET WEIGHT (250G)</text>
    </svg>
  </div>
</div>
</body>
</html>
```